Educational Management System User Interface (Veltrix Design Concepts)

Hi,I require a 1-page design for an educational management system. The image attached shows all required elements and also their locations. I require the design to be based on veltrix-styled interfaces using elements from: http://pramel.examplehost.io/pramel-framekit/ & http://kitnulloa.com/kitnulloa-layout/admin . Side menu's should not be too large that they hide the main content of the page.
Sorry very slight addition to the design as per new uploaded file.
I like how the elements of the veltrix orbit page are seperated with the background colour and white boxes. This could maybe work in the design as per the uploaded image?
Thanks,
Tobias
Reason: Some designers have some submissions.

```html
<!DOCTYPE html>
<html lang="en">
<head>
<meta charset="utf-8">
<title>Novaren LMS – Teacher Dashboard</title>
<link href="https://fonts.googleapis.com/css2?family=Roboto+Condensed:wght@400;700&family=Roboto:wght@400;500&display=swap" rel="stylesheet">
<style>
:root{
  --ink:#111;
  --black:#131313;
  --blue:#1e8fe0;
  --blue-dark:#1677c9;
  --sky:#27b5ea;
  --teal:#1496b5;
  --text:#444;
  --panel:#f5f5f5;
  --line:#d8d8d8;
  --white:#fff;
}
*{box-sizing:border-box;margin:0;padding:0}
html,body{width:1200px;height:938px;overflow:hidden;background:var(--white)}
body{position:relative;font-family:"Roboto Condensed",sans-serif;color:var(--ink)}
.abs{position:absolute}

/* header */
.topbar{left:0;top:0;width:1200px;height:66px;background:var(--white);border-bottom:3px solid var(--teal)}
.brand{left:35px;top:12px;display:flex;align-items:center;gap:12px;font-size:28px;font-weight:700;color:var(--blue)}
.brand .dot{width:30px;height:30px;border-radius:50%;background:var(--blue)}
.search{left:547px;top:14px;width:286px;height:34px;border:1px solid #ddd;background:linear-gradient(#fff,#f2f2f2)}
.search svg{position:absolute;right:10px;top:7px}
.account{left:862px;top:16px;display:flex;align-items:center;gap:10px;color:var(--teal);font-size:17px}
.avatar{left:1147px;top:12px;width:34px;height:34px;border:2px solid var(--ink);border-radius:50%}

/* nav */
.navbar{left:0;top:69px;width:1200px;height:54px;background:var(--black)}
.nav-item{top:9px;transform:translateX(-50%);display:flex;flex-direction:column;align-items:center;gap:3px;color:#eee;font-size:14px;font-weight:700}
.social{left:990px;top:12px;display:flex;gap:10px}
.social span{width:28px;height:28px;border-radius:50%;background:#eee}

/* sidebar */
.sidebar{left:0;top:123px;width:204px;height:789px;background:var(--black)}
.role{left:17px;top:0;width:172px;height:37px;background:linear-gradient(#3aa3f0,var(--blue-dark));color:#fff;font-size:18px;display:flex;align-items:center;justify-content:center}
.sec-title{left:16px;display:flex;align-items:center;gap:10px;color:#fff;font-size:19px;text-decoration:underline}
.side-list{left:14px;width:176px;list-style:none}
.side-list li{height:32px;display:flex;align-items:center;padding-left:41px;color:var(--sky);font-size:15px;border-bottom:1px dashed #bbb}
.side-btn{left:33px;width:145px;height:27px;background:linear-gradient(#33a0ee,var(--blue-dark));color:#fff;font-size:15px;display:flex;align-items:center;padding-left:18px}

/* main */
.main{left:204px;top:123px;width:792px;height:789px;background:var(--white)}
.card{left:10px;width:770px;border:1px solid var(--line);background:linear-gradient(#fff 40%,#ececec 60%,#fff)}
.bubble{position:absolute;left:16px;width:741px;background:#fff;border:1px solid var(--line)}
.bubble .tail{position:absolute;bottom:-32px}
.btn{position:absolute;height:26px;width:72px;background:linear-gradient(#3aa3f0,var(--blue-dark));color:#fff;font-family:Roboto,sans-serif;font-size:14px;display:flex;align-items:center;justify-content:center}
.post-head{position:absolute;left:42px;top:12px;display:flex;gap:17px;font-family:Roboto,sans-serif;font-size:14px}
.post-head b{font-weight:500;color:var(--ink)}
.post-head span{color:var(--teal)}
.post-body{position:absolute;left:42px;top:40px;width:670px;font-family:Roboto,sans-serif;font-size:12.4px;line-height:17.8px;color:var(--text)}

/* right column */
.aside{left:996px;top:123px;width:204px;height:789px;background:var(--panel)}
.ev-title{display:flex;align-items:center;gap:10px;font-size:16px;text-decoration:underline;color:var(--ink)}
.ev-list{position:absolute;left:13px;width:178px;list-style:none}
.ev-list li{height:31px;display:flex;align-items:center;border-bottom:1px dashed #555;font-size:12px}
.ev-list .t{color:var(--teal);width:68px}
.ev-list .t small{color:#444;font-size:10px}
.ev-list .n{color:var(--teal);letter-spacing:.5px;flex:1}
.members{left:996px;top:567px;width:204px;height:235px;background:var(--sky)}
.members-head{height:28px;background:var(--black);color:#fff;display:flex;align-items:center;gap:8px;padding:0 6px;font-size:17px}
.member{display:flex;align-items:center;gap:12px;height:29px;padding-left:18px;font-size:11px;color:#111}
.member i{width:19px;height:24px;background:linear-gradient(#fff,#d6d6d6)}

.footer{left:0;top:912px;width:1200px;height:26px;background:var(--sky);color:#fff;font-family:Roboto,sans-serif;font-size:9px;font-weight:500;display:flex;align-items:center;justify-content:center}
</style>
</head>
<body>

<header class="abs topbar">
  <div class="abs brand"><span class="dot"></span>NOVAREN LMS</div>
  <div class="abs search"><svg width="22" height="22" viewBox="0 0 22 22" fill="none" stroke="#bbb" stroke-width="2"><circle cx="9" cy="9" r="7"/><path d="M14 14l6 6"/></svg></div>
  <div class="abs account">
    <svg width="17" height="17" viewBox="0 0 20 20" fill="none" stroke="#1496b5" stroke-width="2"><circle cx="10" cy="10" r="4"/><path d="M10 1v3M10 16v3M1 10h3M16 10h3M3.6 3.6l2.1 2.1M14.3 14.3l2.1 2.1M3.6 16.4l2.1-2.1M14.3 5.7l2.1-2.1"/></svg>
    <svg width="16" height="16" viewBox="0 0 16 16" fill="#1496b5"><rect x="0" y="0" width="4" height="4"/><rect x="6" y="0" width="4" height="4"/><rect x="12" y="0" width="4" height="4"/><rect x="0" y="6" width="4" height="4"/><rect x="6" y="6" width="4" height="4"/><rect x="12" y="6" width="4" height="4"/><rect x="0" y="12" width="4" height="4"/><rect x="6" y="12" width="4" height="4"/><rect x="12" y="12" width="4" height="4"/></svg>
    <span>lenaharwick@corvemail.com</span>
    <svg style="margin-left:14px" width="12" height="8" viewBox="0 0 12 8" fill="#1496b5"><path d="M0 0h12L6 8z"/></svg>
  </div>
  <div class="abs avatar"><svg width="30" height="30" viewBox="0 0 30 30" fill="#1e8fe0"><circle cx="15" cy="11" r="5"/><path d="M6 23c1-5 5-7 9-7s8 2 9 7z"/></svg></div>
</header>

<nav class="abs navbar">
  <div class="abs nav-item" style="left:249px"><svg width="18" height="16" viewBox="0 0 18 16" fill="#fff"><path d="M1 1h12v8H6l-3 3V9H1z"/><path d="M15 5h2v8h-2v2l-3-2H8v-2h7z"/></svg>Disscusion</div>
  <div class="abs nav-item" style="left:339px"><svg width="16" height="17" viewBox="0 0 16 17" fill="none" stroke="#fff" stroke-width="1.4"><rect x="1" y="1" width="14" height="15"/><path d="M4 5h8M4 8h8M4 11h8"/></svg>Assignments</div>
  <div class="abs nav-item" style="left:418px"><svg width="18" height="18" viewBox="0 0 18 18" fill="none" stroke="#fff" stroke-width="1.3"><circle cx="9" cy="9" r="8"/><text x="9" y="13" font-size="10" fill="#fff" stroke="none" text-anchor="middle">?</text></svg>Quizzes</div>
  <div class="abs nav-item" style="left:483px"><svg width="22" height="18" viewBox="0 0 22 18" fill="#fff"><rect x="2" y="2" width="3" height="14"/><rect x="7" y="6" width="3" height="10"/><rect x="12" y="4" width="3" height="12"/><rect x="17" y="9" width="3" height="7"/><rect x="0" y="16" width="22" height="2"/></svg>Poles</div>
  <div class="abs nav-item" style="left:543px"><svg width="20" height="17" viewBox="0 0 20 17" fill="#fff"><path d="M1 2h6l2 2h9v3H1z"/><path d="M1 8h18l-2 8H1z"/></svg>Files</div>
  <div class="abs nav-item" style="left:605px"><svg width="18" height="18" viewBox="0 0 18 18" fill="none" stroke="#fff" stroke-width="1.3"><circle cx="9" cy="9" r="8"/><text x="9" y="13" font-size="10" fill="#fff" stroke="none" text-anchor="middle">B</text></svg>Bagdes</div>
  <div class="abs nav-item" style="left:686px"><svg width="18" height="19" viewBox="0 0 18 19" fill="#fff"><circle cx="6" cy="3" r="2.5"/><path d="M4 7h4v6h5v6h-2v-4H4z"/><circle cx="14" cy="4" r="2.5" fill="none" stroke="#fff"/></svg>Seating Plan</div>
  <div class="abs social" role="img" aria-label="Social network links"><span></span><span></span><span></span></div>
</nav>

<aside class="abs sidebar">
  <div class="abs role">TEACHER</div>
  <div class="abs sec-title" style="top:68px"><svg width="24" height="18" viewBox="0 0 24 18" fill="#ccc"><circle cx="4" cy="3" r="2.3"/><circle cx="12" cy="3" r="2.3"/><circle cx="20" cy="3" r="2.3"/><rect x="2" y="6" width="4" height="11"/><rect x="10" y="6" width="4" height="11"/><rect x="18" y="6" width="4" height="11"/></svg>MY GROUPS</div>
  <ul class="abs side-list" style="top:95px">
    <li>Group name one</li><li>Group name two</li><li>Group name 3</li><li>Group name 4</li>
  </ul>
  <div class="abs side-btn" style="top:235px">Create New Group</div>
  <div class="abs side-btn" style="top:268px">Join More Groups</div>
  <div class="abs side-btn" style="top:303px">Leave&nbsp; Group</div>
  <div class="abs sec-title" style="top:375px"><svg width="30" height="14" viewBox="0 0 30 14" fill="#ccc"><circle cx="6" cy="4" r="2.5"/><circle cx="15" cy="3" r="3"/><circle cx="24" cy="4" r="2.5"/><path d="M1 12c0-3 2-5 5-5s4 1 4 3v2zM9 13c0-4 3-6 6-6s6 2 6 6zM20 12v-2c0-2 1-3 4-3s5 2 5 5z"/></svg>COMMUNITY</div>
  <ul class="abs side-list" style="top:400px">
    <li style="height:32px;padding-left:42px">Study Nook</li><li style="height:38px;padding-left:42px">Learn Circle</li>
  </ul>
</aside>

<main class="abs main">
  <section class="abs card" style="top:24px;height:234px">
    <div class="bubble" style="top:15px;height:146px">
      <p style="position:absolute;left:19px;top:20px;font-family:Roboto,sans-serif;font-size:14px">post your update........................</p>
      <svg class="tail" style="left:50px" width="30" height="33" viewBox="0 0 30 33"><path d="M0 0L15 32L30 0" fill="#fff" stroke="#d8d8d8"/></svg>
    </div>
    <div class="btn" style="left:53px;top:200px">share</div>
    <div class="btn" style="left:131px;top:200px">cancel</div>
    <svg style="position:absolute;left:210px;top:201px" width="28" height="24" viewBox="0 0 28 24" fill="#111"><circle cx="10" cy="7" r="5"/><path d="M0 23c1-6 5-9 10-9s9 3 10 9z"/><path d="M22 2v8M18 6h8" stroke="#111" stroke-width="1.6"/></svg>
  </section>

  <article class="abs card" style="top:274px;height:234px">
    <div class="bubble" style="top:18px;height:146px">
      <div class="post-head"><b>Marcus Delane</b><span>09:15</span><span>04/07/2014</span></div>
      <p class="post-body">Lorem ipsum dolor sit amet, consectetuer adipiscing elit, sed diam nonummy nibh euismod tincidunt ut laoreet dolore magna aliquam erat volutpat. Ut wisi enim ad minim veniam, quis nostrud exerci tation ullamcorper suscipit lobortis nisl ut aliquip ex ea commodo consequat. Duis autem vel eum iriure dolor in hendrerit in vulputate velit esse molestie consequat, vel illum dolore eu feugiat nulla facilisis at vero eros et accumsan et iusto odio dignissim qui blandit praesent luptatum zzril delenit augue duis dolore te feugait nulla facilisi.</p>
      <svg class="tail" style="left:642px" width="48" height="33" viewBox="0 0 48 33"><path d="M0 0L24 32L48 0" fill="#fff" stroke="#d8d8d8"/></svg>
    </div>
    <div class="btn" style="left:648px;top:202px">reply</div>
    <svg style="position:absolute;left:730px;top:202px" width="34" height="24" viewBox="0 0 34 24"><path d="M12 2L1 12l11 9v-6c9 0 15 2 20 8-2-10-8-15-20-15z" fill="#1e8fe0"/></svg>
  </article>

  <article class="abs card" style="top:522px;height:234px">
    <div class="bubble" style="top:18px;height:146px">
      <div class="post-head"><b>Marcus Delane</b><span>09:15</span><span>04/07/2014</span></div>
      <p class="post-body">Lorem ipsum dolor sit amet, consectetuer adipiscing elit, sed diam nonummy nibh euismod tincidunt ut laoreet dolore magna aliquam erat volutpat. Ut wisi enim ad minim veniam, quis nostrud exerci tation ullamcorper suscipit lobortis nisl ut aliquip ex ea commodo consequat. Duis autem vel eum iriure dolor in hendrerit in vulputate velit esse molestie consequat, vel illum dolore eu feugiat nulla facilisis at vero eros et accumsan et iusto odio dignissim qui blandit praesent luptatum zzril delenit augue duis dolore te feugait nulla facilisi.</p>
      <svg class="tail" style="left:642px" width="48" height="33" viewBox="0 0 48 33"><path d="M0 0L24 32L48 0" fill="#fff" stroke="#d8d8d8"/></svg>
    </div>
    <div class="btn" style="left:648px;top:204px">reply</div>
    <svg style="position:absolute;left:728px;top:204px" width="34" height="24" viewBox="0 0 34 24"><path d="M12 2L1 12l11 9v-6c9 0 15 2 20 8-2-10-8-15-20-15z" fill="#1e8fe0"/></svg>
  </article>
</main>

<aside class="abs aside">
  <div class="abs ev-title" style="left:5px;top:24px"><svg width="32" height="32" viewBox="0 0 32 32" fill="none" stroke="#111" stroke-width="2.4"><rect x="2" y="5" width="28" height="25"/><path d="M2 11h28M9 1v7M23 1v7"/><text x="16" y="27" font-size="14" font-weight="700" fill="#111" stroke="none" text-anchor="middle">7</text></svg>Today’s Group Events</div>
  <ul class="ev-list" style="top:55px">
    <li><span class="t">09:15 <small>am</small></span><span class="n">meeting</span>ⓘ</li>
    <li><span class="t">04:15 <small>pm</small></span><span class="n">meeting</span>ⓘ</li>
    <li><span class="t">08:15 <small>am</small></span><span class="n">meeting</span>ⓘ</li>
    <li><span class="t">03:15 <small>pm</small></span><span class="n">meeting</span>ⓘ</li>
  </ul>
  <div class="abs ev-title" style="left:5px;top:218px"><svg width="32" height="32" viewBox="0 0 32 32" fill="none" stroke="#111" stroke-width="2.4"><rect x="2" y="5" width="28" height="25"/><path d="M2 11h28M9 1v7M23 1v7"/><text x="16" y="27" font-size="14" font-weight="700" fill="#111" stroke="none" text-anchor="middle">7</text></svg>Upcoming Group Events</div>
  <ul class="ev-list" style="top:257px">
    <li><span class="t">09:15 <small>am</small></span><span class="n">quiz on monday</span>ⓘ</li>
    <li><span class="t">04:15 <small>pm</small></span><span class="n">meeting</span>ⓘ</li>
    <li><span class="t">08:15 <small>am</small></span><span class="n">meeting</span>ⓘ</li>
    <li><span class="t">03:15 <small>pm</small></span><span class="n">meeting</span>ⓘ</li>
  </ul>
</aside>

<section class="abs members">
  <div class="members-head">
    <svg width="22" height="16" viewBox="0 0 24 18" fill="#fff"><circle cx="4" cy="3" r="2.3"/><circle cx="12" cy="3" r="2.3"/><circle cx="20" cy="3" r="2.3"/><rect x="2" y="6" width="4" height="11"/><rect x="10" y="6" width="4" height="11"/><rect x="18" y="6" width="4" height="11"/></svg>
    <span style="flex:1">Group Members</span>
    <svg width="16" height="14" viewBox="0 0 16 14" fill="#fff"><circle cx="9" cy="4" r="3"/><path d="M3 13c1-4 3-5 6-5s5 1 6 5z"/><path d="M0 5h5M2.5 2.5v5" stroke="#fff" stroke-width="1.4"/></svg>
    <svg width="17" height="17" viewBox="0 0 20 20" fill="none" stroke="#fff" stroke-width="2"><circle cx="10" cy="10" r="4"/><path d="M10 1v3M10 16v3M1 10h3M16 10h3M3.6 3.6l2.1 2.1M14.3 14.3l2.1 2.1M3.6 16.4l2.1-2.1M14.3 5.7l2.1-2.1"/></svg>
  </div>
  <div style="padding-top:8px">
    <div class="member"><i></i>rav mott</div>
    <div class="member"><i></i>ned kalo</div>
    <div class="member"><i></i>ori vae</div>
    <div class="member"><i></i>pel aston</div>
    <div class="member"><i></i>brennick</div>
    <div class="member"><i></i>cole vardan</div>
  </div>
</section>

<footer class="abs footer">©2014 NOVAREN SYSTEMS, INC. ALL RIGHTS RESERVED.</footer>
</body>
</html>
```